Broschüren für Kinderteppich Kollektion
Zielgruppe
TAMURO.DE aus Herxheim in der Pfalz will Spiel und Spaß im Kinderzimmer: Wir bieten Ihnen hochwertige und kreative Teppiche für Kinder und Jugendliche, sowie farbenfrohe und trendige Spielteppiche.
Aufgabenstellung
Wir planen einen Broschüre für unsere Kollektion ' Pebble line' handgemachte Kinderteppiche aus Wolle und Baumwolle. B2B Bereich.
Wenig Text..große Bilder und alles in sehr schlichtem Design.
Das Druckmass sollte DIN A5 oder quadratisch sein.
Umfang ca. 15-20 Designs in verschiedenen Farbkombinationen. Teppiche werden im Plattschuss gezeigt..und ergänzt durch Nahaufnahmen der Struktur.
Wir sind nun in der Planung soweit, das wir die Broschüre quadratisch machen, wie auch die meisten bevorzugen.
Seitenanzahl wird mit Umschlag 20 Seiten sein.Designanzahl nun exact:
1) Wolle handmade: : Swirlmix in drei Farben, Moonkite in drei Farben, und neue Designs: Design: WAVE: in 8 Farben und design BLOOM in drei Farben:
Insgesamt Wolle 17 Farbstellungen und das jeweils in drei Größen.
2) Baumwolle : Maple in drei Farben und zwei Größen.
Fotos sind alle Hochauflösend vorhanden. ( NEUE Kollektion WAVE und BLOOM sind gerade beim fotographieren)

```html
<!DOCTYPE html>
<html lang="de">
<head>
<meta charset="utf-8">
<title>Tamuro – Pebble Line Broschüre</title>
<link href="https://fonts.googleapis.com/css2?family=Cabin:wght@400;600&family=Cabin+Sketch:wght@400;700&display=swap" rel="stylesheet">
<style>
:root{
  --bg:#c4a9b8;
  --paper:#ffffff;
  --ink:#6e6a6c;
  --ink-light:#a29ea0;
  --orange:#e97f2c;
  --pink:#c98c9d;
  --pink-soft:#e7cfd6;
  --blue:#5b8ec3;
  --grey-band:#dedad8;
  --teal-band:#cbd6d7;
  --table-row:#efeeee;
  --table-head:#dcdadb;
  --lilac:#b889b8;
}
*{margin:0;padding:0;box-sizing:border-box}
html,body{width:1200px;height:257px;overflow:hidden;background:var(--bg)}
body{position:relative;font-family:"Cabin",sans-serif;color:var(--ink)}
.spread{position:absolute;top:50px;width:305px;height:154px;display:flex;box-shadow:0 2px 6px rgba(80,50,70,.25)}
.spread--overview{left:48px}
.spread--swirlmix{left:450px}
.spread--moonkite{left:850px}
.page{position:relative;width:152.5px;height:154px;background:var(--paper);overflow:hidden}
.page--left{box-shadow:inset -4px 0 6px -4px rgba(0,0,0,.15)}
.page--right{box-shadow:inset 4px 0 6px -4px rgba(0,0,0,.15)}
.photo{position:absolute;display:block}
.brand{position:absolute;left:9px;top:7px;display:flex;align-items:center;gap:2px;background:var(--paper);padding:2px 3px}
.brand__mark{width:6px;height:6px;background:var(--orange)}
.brand__name{font-family:"Cabin",sans-serif;font-weight:600;font-size:7px;color:var(--orange);letter-spacing:.3px}
.title{position:absolute;left:10px;font-family:"Cabin Sketch",sans-serif;font-weight:700;line-height:1}
.sub{position:absolute;left:10px;font-size:3.4px;color:var(--ink-light);line-height:1.35}
.page-no{position:absolute;right:6px;bottom:5px;width:7px;height:7px;background:var(--orange);color:#fff;font-size:2.6px;display:flex;align-items:center;justify-content:center}
.material{position:absolute;display:flex;flex-direction:column;align-items:center;gap:1px;font-size:2.4px;color:var(--ink-light)}
.material__dot{width:7px;height:7px;border-radius:50%}
/* overview table */
.rug-table{position:absolute;left:10px;top:38px;width:133px;border-collapse:collapse;font-size:2.4px;color:var(--ink-light)}
.rug-table th{background:var(--table-head);text-align:left;font-weight:400;padding:1.2px 1.5px;color:var(--ink)}
.rug-table td{background:var(--table-row);padding:1.1px 1.5px;border-bottom:.4px solid #fff}
.rug-table tr.gap td{background:none;height:2.5px;padding:0;border:0}
.rug-table td.price{text-align:right}
.bullet{display:inline-block;width:3px;height:3px;border-radius:50%;background:var(--orange);margin-right:.5px;vertical-align:middle}
.bullet--lilac{background:var(--lilac)}
.footnote{position:absolute;left:10px;top:142px;width:120px;font-size:2.2px;color:var(--ink-light)}
/* product pages */
.band{position:absolute;left:0;right:0;bottom:0}
.band__text{position:absolute;left:8px;width:62px;font-size:2.6px;line-height:1.4;color:#fff}
.sizes{position:absolute;left:8px;font-size:2.5px;color:#fff;border-collapse:collapse}
.sizes td{padding:.6px 3px .6px 0}
.callout{position:absolute;font-size:2.4px;color:var(--ink-light);line-height:1.3}
.callout::after{content:"";position:absolute;left:0;top:100%;width:.4px;height:6px;background:var(--ink-light)}
.rug{position:absolute;box-shadow:1px 2px 4px rgba(0,0,0,.25)}
.zoom{position:absolute;border-radius:50%;border:1.2px solid #fff;box-shadow:0 1px 3px rgba(0,0,0,.35)}
</style>
</head>
<body>

<!-- Spread 1: overview -->
<section class="spread spread--overview">
  <div class="page page--left">
    <div class="photo" role="img" aria-label="Nahaufnahme eines rosafarbenen Wollteppichs mit umgeschlagener Ecke und Noppe" style="left:9px;top:5px;width:88px;height:73px;background:linear-gradient(135deg,#c9aeb5,#b598a0)"></div>
    <div class="photo" role="img" aria-label="Detail grauer Teppich mit Punkten" style="left:99px;top:5px;width:43px;height:35px;background:linear-gradient(135deg,#a8acad,#8d9293)"></div>
    <div class="photo" role="img" aria-label="Detail heller Teppich mit grauen Sternen" style="left:99px;top:42px;width:43px;height:36px;background:linear-gradient(135deg,#d9d6d1,#8a8d90)"></div>
    <div class="photo" role="img" aria-label="Naturweißer Teppich mit umgeschlagener Kante" style="left:9px;top:80px;width:44px;height:68px;background:linear-gradient(135deg,#d8d2c6,#b9b2a5)"></div>
    <div class="photo" role="img" aria-label="Heller Teppich mit blauen und grauen Sternen" style="left:55px;top:80px;width:87px;height:68px;background:linear-gradient(135deg,#ddd9d2,#6f8198)"></div>
    <div class="brand"><span class="brand__mark"></span><span class="brand__name">TAMURO</span></div>
  </div>
  <div class="page page--right">
    <h1 class="title" style="top:24px;font-size:6px;color:var(--orange)">Pebble Line</h1>
    <p class="sub" style="top:31px;color:var(--ink)">Unsere Kinderteppiche in der Übersicht</p>
    <div class="material" style="left:114px;top:22px"><span class="material__dot" style="background:#f2b27a"></span>Wolle</div>
    <div class="material" style="left:126px;top:22px"><span class="material__dot" style="background:#d7b4d6"></span>Baumw.</div>
    <table class="rug-table">
      <tr><th></th><th>Modell</th><th>Maße</th><th>Farbvarianten</th><th class="price">Netto in EUR</th></tr>
      <tr><td><span class="bullet"></span></td><td>Swirlmix</td><td>100 x 160 cm</td><td>flieder/multi, grau/multi, natur</td><td class="price">190,00 €</td></tr>
      <tr><td><span class="bullet"></span></td><td>Swirlmix</td><td>120 x 180 cm</td><td>flieder/multi, grau/multi, natur</td><td class="price">230,00 €</td></tr>
      <tr><td><span class="bullet"></span></td><td>Swirlmix</td><td>160 x 230 cm</td><td>flieder/multi, grau/multi, natur</td><td class="price">330,00 €</td></tr>
      <tr class="gap"><td colspan="5"></td></tr>
      <tr><td><span class="bullet"></span></td><td>Moonkite</td><td>100 x 160 cm</td><td>natur/blau, natur/grau, rosa</td><td class="price">190,00 €</td></tr>
      <tr><td><span class="bullet"></span></td><td>Moonkite</td><td>120 x 180 cm</td><td>natur/blau, natur/grau, rosa</td><td class="price">230,00 €</td></tr>
      <tr class="gap"><td colspan="5"></td></tr>
      <tr><td><span class="bullet"></span><span class="bullet bullet--lilac"></span></td><td>Wave</td><td>100 x 160 cm</td><td>flieder, blau, grau, rot, grün, natur</td><td class="price">ab 190,00 €</td></tr>
      <tr><td><span class="bullet"></span><span class="bullet bullet--lilac"></span></td><td>Wave</td><td>120 x 180 cm</td><td>flieder, blau, grau, rot, grün, natur</td><td class="price">ab 230,00 €</td></tr>
      <tr><td><span class="bullet"></span><span class="bullet bullet--lilac"></span></td><td>Wave</td><td>160 x 230 cm</td><td>flieder, blau, grau, rot, grün, natur</td><td class="price">ab 330,00 €</td></tr>
      <tr class="gap"><td colspan="5"></td></tr>
      <tr><td><span class="bullet"></span><span class="bullet bullet--lilac"></span></td><td>Bloom</td><td>100 x 160 cm</td><td>flieder/multi, grau/multi, natur</td><td class="price">ab 190,00 €</td></tr>
      <tr><td><span class="bullet"></span><span class="bullet bullet--lilac"></span></td><td>Bloom</td><td>120 x 180 cm</td><td>flieder/multi, grau/multi, natur</td><td class="price">ab 230,00 €</td></tr>
      <tr><td><span class="bullet"></span><span class="bullet bullet--lilac"></span></td><td>Bloom</td><td>160 x 230 cm</td><td>flieder/multi, grau/multi, natur</td><td class="price">ab 330,00 €</td></tr>
      <tr class="gap"><td colspan="5"></td></tr>
      <tr><td><span class="bullet bullet--lilac"></span></td><td>Maple</td><td>60 x 110 cm</td><td>blau, grau, rosa</td><td class="price">190,00 €</td></tr>
      <tr><td><span class="bullet bullet--lilac"></span></td><td>Maple</td><td>90 x 160 cm</td><td>blau, grau, rosa</td><td class="price">230,00 €</td></tr>
    </table>
    <p class="footnote">Alle Preise netto zzgl. Versand. Farben können leicht vom Druck abweichen, Maße ca. Angaben.</p>
    <span class="page-no">02</span>
  </div>
</section>

<!-- Spread 2: Swirlmix -->
<section class="spread spread--swirlmix">
  <div class="page page--left">
    <div class="brand"><span class="brand__mark"></span><span class="brand__name">TAMURO</span></div>
    <h2 class="title" style="top:44px;font-size:12px;color:var(--pink)">Swirlmix</h2>
    <p class="sub" style="top:58px">Sunny Rugs for Kids<br>Schurwoll Teppich Sunny Rugs</p>
    <div class="material" style="left:10px;top:82px"><span class="material__dot" style="background:var(--orange)"></span>Schurwolle</div>
    <div class="band" style="top:96px;background:var(--pink)">
      <p class="band__text" style="top:8px">Die Teppiche sind aus reiner Wolle handgefertigt und sehr weich im Griff. Zwei Webtechniken verbinden sich zu einem lebendigen 3D Design für den Boden.</p>
      <table class="sizes" style="top:34px">
        <tr><td>Größe A</td><td>100 x 160 cm</td><td>190,00 €</td></tr>
        <tr><td>Größe B</td><td>120 x 180 cm</td><td>230,00 €</td></tr>
        <tr><td>Größe C</td><td>160 x 230 cm</td><td>330,00 €</td></tr>
      </table>
    </div>
    <span class="callout" style="left:107px;top:34px">Farbe:<br>flieder/multi</span>
    <div class="rug" role="img" aria-label="Fliederfarbener Teppich mit bunten Punkten im Plattschuss" style="left:73px;top:42px;width:69px;height:103px;background:linear-gradient(160deg,#e2cdd4,#cfb3bd)"></div>
    <div class="zoom" role="img" aria-label="Nahaufnahme der Teppichstruktur mit Noppe" style="left:70px;top:76px;width:30px;height:30px;background:linear-gradient(135deg,#c7b0b8,#8f8186)"></div>
  </div>
  <div class="page page--right">
    <div class="band" style="top:97px;background:var(--grey-band)"></div>
    <span class="callout" style="left:16px;top:26px">Farbe:<br>grau/multi</span>
    <span class="callout" style="left:100px;top:36px">Farbe:<br>natur/multi</span>
    <div class="rug" role="img" aria-label="Grauer Teppich mit bunten Punkten" style="left:12px;top:38px;width:62px;height:90px;transform:rotate(-6deg);background:linear-gradient(160deg,#b5b3b3,#9c9a9a)"></div>
    <div class="rug" role="img" aria-label="Naturweißer Teppich mit bunten Punkten" style="left:80px;top:48px;width:62px;height:90px;transform:rotate(6deg);background:linear-gradient(160deg,#f1efea,#dedbd4)"></div>
    <div class="zoom" role="img" aria-label="Nahaufnahme grauer Teppich" style="left:8px;top:110px;width:30px;height:30px;background:linear-gradient(135deg,#a9a8a8,#7d7c7c)"></div>
    <div class="zoom" role="img" aria-label="Nahaufnahme naturweißer Teppich" style="left:114px;top:88px;width:30px;height:30px;background:linear-gradient(135deg,#ece8df,#c7c1b5)"></div>
    <span class="page-no">05</span>
  </div>
</section>

<!-- Spread 3: Moonkite -->
<section class="spread spread--moonkite">
  <div class="page page--left">
    <div class="brand"><span class="brand__mark"></span><span class="brand__name">TAMURO</span></div>
    <h2 class="title" style="top:44px;font-size:12px;color:var(--blue)">Moonkite</h2>
    <p class="sub" style="top:58px">Sunny Rugs for Kids<br>Schurwoll Teppich Sunny Rugs</p>
    <div class="material" style="left:10px;top:82px"><span class="material__dot" style="background:var(--orange)"></span>Schurwolle</div>
    <div class="band" style="top:98px;background:var(--blue)">
      <p class="band__text" style="top:8px">Die Teppiche sind aus reiner Wolle handgefertigt und sehr weich im Griff. Zwei Webtechniken verbinden sich zu einem lebendigen 3D Design für den Boden.</p>
      <table class="sizes" style="top:34px">
        <tr><td>Größe A</td><td>100 x 160 cm</td><td>190,00 €</td></tr>
        <tr><td>Größe B</td><td>120 x 180 cm</td><td>230,00 €</td></tr>
      </table>
    </div>
    <span class="callout" style="left:110px;top:28px">Farbe:<br>natur/blau-grau</span>
    <div class="rug" role="img" aria-label="Naturweißer Teppich mit blauen und grauen Sternen" style="left:78px;top:38px;width:68px;height:100px;transform:rotate(5deg);background:linear-gradient(160deg,#e9e6e0,#8193a9)"></div>
    <div class="zoom" role="img" aria-label="Nahaufnahme blauer Stern" style="left:70px;top:76px;width:30px;height:30px;background:linear-gradient(135deg,#d8d6d2,#4f6a92)"></div>
  </div>
  <div class="page page--right">
    <div class="band" style="top:98px;background:var(--teal-band)"></div>
    <span class="callout" style="left:46px;top:24px">Farbe:<br>natur/grau</span>
    <span class="callout" style="left:126px;top:40px">Farbe:<br>natur/rosa</span>
    <div class="rug" role="img" aria-label="Naturweißer Teppich mit grauen Sternen" style="left:12px;top:36px;width:62px;height:90px;transform:rotate(-6deg);background:linear-gradient(160deg,#eeebe6,#b7b7b8)"></div>
    <div class="rug" role="img" aria-label="Naturweißer Teppich mit rosa Sternen" style="left:78px;top:48px;width:62px;height:90px;transform:rotate(6deg);background:linear-gradient(160deg,#f1ece9,#d7a8b8)"></div>
    <div class="zoom" role="img" aria-label="Nahaufnahme grauer Stern" style="left:10px;top:110px;width:30px;height:30px;background:linear-gradient(135deg,#d3d1cd,#7c7e80)"></div>
    <div class="zoom" role="img" aria-label="Nahaufnahme rosa Stern" style="left:116px;top:70px;width:30px;height:30px;background:linear-gradient(135deg,#eadfe0,#c48a9c)"></div>
    <span class="page-no">06</span>
  </div>
</section>

</body>
</html>
```